Investment company needing business card

We are wanting a business card which looks sharp and easy on the eye. We are thinking of having a business card with the logo embossed on it, to really make it stand out. We will only have a small amount of information of the business card, person's name, position, email address and phone number

Contact Information for Business Card

Danica Pruett
Executive Assistant
+64 21 547 3162
danicap@harwellcapital.co.nz

Requirements
Must have
• Embossed logo
Should not have
• Not to be busy

```html
<!DOCTYPE html>
<html lang="en">
<head>
<meta charset="utf-8">
<title>Harwell Capital — Business Card</title>
<link rel="stylesheet" href="https://fonts.googleapis.com/css2?family=Montserrat:wght@700&family=Open+Sans:wght@400;600;700&display=swap">
<style>
  :root {
    --brand-green: #22b573;
    --ink-grey: #555a5e;
    --rule-grey: #6b6f72;
    --paper: #ffffff;
    --backdrop: #e6e8e7;
  }
  * { margin: 0; padding: 0; box-sizing: border-box; }
  html, body { width: 1200px; height: 900px; overflow: hidden; }
  body { background: var(--backdrop); position: relative; font-family: "Open Sans", sans-serif; }

  .card { position: absolute; width: 620px; height: 360px; border-radius: 22px; }

  /* Front */
  .card-front { left: 110px; top: 60px; background: var(--brand-green); padding: 20px; }
  .card-front .face {
    position: relative; width: 100%; height: 100%;
    background: var(--paper); border-radius: 16px;
  }
  .brand { display: flex; align-items: center; gap: 12px; }
  .brand-square { width: 34px; height: 34px; }
  .brand-name {
    font-family: "Montserrat", sans-serif; font-weight: 700;
    font-size: 30px; letter-spacing: 1px; line-height: 1;
  }
  .card-front .brand { position: absolute; left: 36px; top: 62px; }
  .card-front .brand-square { background: var(--brand-green); }
  .card-front .brand-name { color: var(--brand-green); }

  .person { position: absolute; right: 36px; top: 112px; text-align: right; }
  .person-name { color: var(--brand-green); font-weight: 700; font-size: 19px; letter-spacing: .3px; }
  .person-role { color: var(--ink-grey); font-size: 15px; margin-top: 2px; }
  .divider { position: absolute; left: 36px; right: 196px; top: 160px; height: 1px; background: var(--rule-grey); }

  .contacts { position: absolute; left: 36px; bottom: 30px; list-style: none; }
  .contacts li { display: flex; align-items: center; gap: 10px; color: var(--ink-grey); font-size: 16px; line-height: 26px; }
  .contacts svg { width: 13px; height: 13px; fill: var(--brand-green); flex: none; }

  /* Back */
  .card-back { left: 470px; top: 480px; background: var(--brand-green); }
  .inner-frame { position: absolute; inset: 16px; border: 1.5px solid rgba(255,255,255,.85); border-radius: 14px; }
  .edge-bar { position: absolute; width: 7px; height: 80px; background: var(--paper); }
  .edge-bar.right { right: 13px; top: 56px; }
  .edge-bar.left { left: 13px; bottom: 56px; }
  .card-back .brand { position: absolute; left: 50%; top: 50%; transform: translate(-50%, -50%); }
  .card-back .brand-square { background: var(--paper); width: 44px; height: 44px; }
  .card-back .brand-name { color: var(--paper); font-size: 38px; }
</style>
</head>
<body>
  <section class="card card-front">
    <div class="face">
      <div class="brand">
        <span class="brand-square"></span>
        <span class="brand-name">HARWELL CAPITAL</span>
      </div>
      <div class="person">
        <div class="person-name">DANICA PRUETT</div>
        <div class="person-role">Executive Assistant</div>
      </div>
      <div class="divider"></div>
      <ul class="contacts">
        <li>
          <svg viewBox="0 0 16 16"><path d="M3.5 1.5l3 3-1.8 1.8a9 9 0 0 0 5 5l1.8-1.8 3 3-2 2C7 14 2 9 1.5 3.5z"/></svg>
          +64 21 547 3162
        </li>
        <li>
          <svg viewBox="0 0 16 16"><path d="M1 3h14v10H1z M1.5 3.5L8 9l6.5-5.5" stroke="#fff" stroke-width="1.2"/></svg>
          danicap@harwellcapital.co.nz
        </li>
        <li>
          <svg viewBox="0 0 16 16"><circle cx="8" cy="8" r="7"/><path d="M1 8h14M8 1c-3 3.5-3 10.5 0 14M8 1c3 3.5 3 10.5 0 14" stroke="#fff" stroke-width="1" fill="none"/></svg>
          www.harwellcapital.co.nz
        </li>
      </ul>
    </div>
  </section>

  <section class="card card-back">
    <div class="inner-frame"></div>
    <span class="edge-bar right"></span>
    <span class="edge-bar left"></span>
    <div class="brand">
      <span class="brand-square"></span>
      <span class="brand-name">HARWELL CAPITAL</span>
    </div>
  </section>
</body>
</html>
```